Flyer Design Project for our Parenting Psychologists at the Bright Harbour Wellbeing Clinic

At the Bright Harbour Wellbeing Clinic we have expert Parenting Psychologists.

Parenting Psychologists provide practical, step by step assistance to parents who are struggling with their children's behavioural and emotional problems.

We need a DL size brochure that will be appealing to parents. The brochure will be on show in schools, kindergartens and GP clinics.

In terms of style it will be in line with our website and stationery that I will attach.

www.brightharbourwellbeing.com.au
Updates

Hi Everyone,
Thanks for putting forward your proposals, there are a couple there that I am very interested in. I am looking to see if there is a way that I can change my brief to guaranteed as I am definitely going to be using one of the designs for sure.
I have emailed ArtFolkly and as soon as I get an answer I will change it if I can.
If anyone out there already knows the answer please let me know :-)
Thanks,
Marnie.

Hi Again,

I worked it out myself!!

I have now changed this to a committed project.

Kind regards,
Marnie.

Reason: I have 46 designs now and need more time to work out which is best!

Target Market(s)

The target will be educated professional parents motivated to get professional help. And doctors and teachers who will pass on the brochures 2 parents

Industry/Entity Type

Health

Requirements
Must have
• I want one DL size brochure. Back and front.

We need text (below) and our contact details. Our logo.

9362 4158
Suite 4, 2071 Pellbrook Rd, Ferndale Heights 3482

Text:
Parents want the best for their kids. They want kids that are happy, healthy and well behaved.

So why is it so hard? Parents of toddlers, primary schoolers and teenagers alike say that they are frustrated by constant nagging, bribing and yelling, they don't know what to try next. Some parents worry that their children are unhappy. Struggling at school, not making friends or coping with bigger problems.

The good news is that getting your children to behave more co-operatively doesn't need to be difficult or mysterious. We all know that kids don't come with manuals, but there are skills every parent can learn to make parenting easier. In a few sessions with a Parenting Psychologist, you will receive step by step guidance in how to talk to your children in a way that will be much more effective getting them to behave in a respectful and co-operative way around the home and in public. You will learn how to help your child cope with problems they are going through. They can help you reconnect with your kids so you can enjoy being a parent again.

Nice to have
• Themes consistent with our website
and letterhead, business cards. I will attach these.
Should not have
• I don't want it to look too cluttered so if the text I have provided up above looks too crowded then I will edit it.

```html
<!DOCTYPE html>
<html lang="en">
<head>
<meta charset="utf-8">
<title>Bright Harbour Wellbeing Clinic – DL Brochure</title>
<link href="https://fonts.googleapis.com/css2?family=Lato:wght@300;400;700&display=swap" rel="stylesheet">
<style>
  :root {
    --page-bg: #eef0f1;
    --panel-white: #fbfbfb;
    --panel-grey: #e5e7e7;
    --teal: #7cc3c6;
    --teal-text: #5fa9a8;
    --slate: #8796a2;
    --steel-blue: #7ba8b8;
    --footer-blue: #8db4c2;
    --lavender: #d3d8ec;
    --ink: #3d4247;
    --ink-soft: #5a5f64;
    --logo-grey: #a9adb0;
    --rule: #d8dbdc;
  }
  * { box-sizing: border-box; margin: 0; padding: 0; }
  html, body { width: 1200px; height: 795px; overflow: hidden; }
  body {
    background: var(--page-bg);
    font-family: "Lato", Arial, sans-serif;
    color: var(--ink);
    display: flex;
    justify-content: center;
    align-items: center;
    gap: 56px;
  }
  .panel {
    width: 340px;
    height: 720px;
    position: relative;
    display: flex;
    flex-direction: column;
    box-shadow: 0 2px 10px rgba(0,0,0,0.08);
    overflow: hidden;
  }
  .stripe { display: flex; height: 12px; flex-shrink: 0; }
  .stripe span { flex: 1; }
  .stripe .s-teal { background: var(--teal); }
  .stripe .s-slate { background: var(--slate); }
  .stripe .s-blue { background: var(--steel-blue); }

  /* Back panel */
  .back-panel { background: var(--panel-white); }
  .back-intro {
    padding: 34px 26px 22px;
    color: var(--teal-text);
    font-size: 19px;
    font-weight: 400;
    line-height: 1.22;
    border-bottom: 1px solid var(--rule);
  }
  .back-body { padding: 22px 26px 0; flex: 1; }
  .back-heading {
    font-size: 16px;
    font-weight: 700;
    letter-spacing: 0.2px;
    color: var(--ink);
    margin-bottom: 14px;
  }
  .back-body p {
    font-size: 11.6px;
    line-height: 1.5;
    color: var(--ink-soft);
  }
  .back-body p + p {
    border-top: 1px solid var(--rule);
    margin-top: 14px;
    padding-top: 14px;
  }
  .back-footer {
    height: 70px;
    flex-shrink: 0;
    background: var(--footer-blue);
    color: #ffffff;
    font-size: 14px;
    display: flex;
    align-items: center;
    justify-content: center;
    position: relative;
  }
  .back-footer::before {
    content: "";
    position: absolute;
    top: 0; left: 0; right: 0; height: 8px;
    background: linear-gradient(90deg, var(--teal) 0 40%, var(--steel-blue) 40% 100%);
  }

  /* Front panel */
  .front-panel { background: var(--panel-grey); }
  .brand-block {
    height: 176px;
    flex-shrink: 0;
    display: flex;
    align-items: center;
    padding: 0 30px;
    gap: 16px;
  }
  .brand-dot {
    width: 48px; height: 48px;
    border-radius: 50%;
    border: 2px solid var(--logo-grey);
    flex-shrink: 0;
  }
  .brand-name {
    font-size: 17px;
    font-weight: 300;
    letter-spacing: 3px;
    text-transform: uppercase;
    color: var(--logo-grey);
    line-height: 1.3;
  }
  .cover-photo {
    height: 250px;
    flex-shrink: 0;
    background: linear-gradient(160deg, #6f9a4a 0%, #9cc26a 40%, #c9a07c 70%, #5f8a3c 100%);
  }
  .photo-rule {
    height: 12px;
    flex-shrink: 0;
    background: linear-gradient(90deg, var(--teal) 0 55%, var(--slate) 55% 78%, var(--teal) 78% 100%);
  }
  .contact-area { flex: 1; position: relative; padding: 26px 18px 0; }
  .contact-shape { position: absolute; left: 14px; top: 26px; width: 312px; height: 200px; }
  .contact-details {
    position: relative;
    padding: 84px 0 0 28px;
    font-size: 13.5px;
    line-height: 1.35;
    color: var(--ink-soft);
  }
  .contact-details .tel-label { font-weight: 700; color: var(--ink); margin-right: 8px; }
</style>
</head>
<body>

  <section class="panel back-panel">
    <div class="stripe"><span class="s-blue"></span><span class="s-teal"></span><span class="s-slate"></span><span class="s-teal"></span></div>
    <p class="back-intro">Parents want the best for their kids. They want kids that are happy, healthy and well behaved.</p>
    <div class="back-body">
      <h2 class="back-heading">SO WHY IS IT SO HARD?</h2>
      <p>Parents of toddlers, primary schoolers and teenagers alike say that they are frustrated by constant nagging, bribing and yelling, they don't know what to try next. Some parents worry that their children are unhappy. Struggling at school, not making friends or coping with bigger problems.</p>
      <p>The good news is that getting your children to behave more co-operatively doesn't need to be difficult or mysterious. We all know that kids don't come with manuals, but there are skills every parent can learn to make parenting easier. In a few sessions with a Parenting Psychologist, you will receive step by step guidance in how to talk to your children in a way that will be much more effective getting them to behave in a respectful and co-operative way around the home and in public. You will learn how to help your child cope with problems they are going through. They can help you reconnect with your kids so you can enjoy being a parent again.</p>
    </div>
    <footer class="back-footer">www.brightharbourwellbeing.com.au</footer>
  </section>

  <section class="panel front-panel">
    <div class="stripe"><span class="s-teal"></span><span class="s-slate"></span><span class="s-teal"></span><span class="s-blue"></span></div>
    <div class="brand-block">
      <span class="brand-dot"></span>
      <span class="brand-name">Bright Harbour Wellbeing Clinic</span>
    </div>
    <div class="cover-photo" role="img" aria-label="Photo of a mother and young child sharing a picnic on a sunny lawn"></div>
    <div class="photo-rule"></div>
    <div class="contact-area">
      <svg class="contact-shape" viewBox="0 0 312 200" aria-hidden="true">
        <path d="M40 40 L250 0 L312 40 L312 150 L40 200 Q0 200 0 160 L0 80 Q0 44 40 40 Z" fill="var(--lavender)"/>
      </svg>
      <div class="contact-details">
        <p><span class="tel-label">tel</span>9362 4158</p>
        <p>Suite 4, 2071 Pellbrook Rd</p>
        <p>Ferndale Heights 3482</p>
        <p>www.brightharbourwellbeing.com.au</p>
      </div>
    </div>
    <div class="stripe"><span class="s-slate"></span><span class="s-teal"></span><span class="s-blue"></span><span class="s-teal"></span></div>
  </section>

</body>
</html>
```